Kiteloft Namecard

We have a regular but rotating group of Actors and Directors who meet weekly. I'd like to make a nametag (first and last names) for each of the participants which would fit on a regular business card. The first name would be over-sized to enable reading at a distance. The background & border should project fun and warmth. The Kiteloft is meant to be a place to play without judgement or negative vibes.

```html
<!DOCTYPE html>
<html lang="en">
<head>
<meta charset="utf-8">
<title>Kiteloft Namecard</title>
<link rel="stylesheet" href="https://fonts.googleapis.com/css2?family=Oswald:wght@400&family=Archivo+Black&family=Michroma&display=swap">
<style>
  :root {
    --brand-red: #a00000;
    --paper: #ffffff;
    --frame: #000000;
    --last-name-grey: #3d3d3d;
  }
  html, body {
    margin: 0;
    padding: 0;
    width: 828px;
    height: 1200px;
    overflow: hidden;
    background: var(--paper);
  }
  .namecard {
    display: block;
    width: 828px;
    height: 1200px;
  }
  .namecard__frame { fill: var(--paper); stroke: var(--frame); stroke-width: 7; }
  .namecard__band,
  .namecard__bubble-tail,
  .namecard__base { fill: var(--brand-red); }
  .namecard__hashtag {
    font-family: "Michroma", sans-serif;
    font-size: 42px;
    fill: var(--brand-red);
  }
  .namecard__first-name {
    font-family: "Oswald", sans-serif;
    font-weight: 400;
    font-size: 480px;
    fill: var(--paper);
  }
  .namecard__last-name {
    font-family: "Archivo Black", sans-serif;
    font-size: 150px;
    fill: var(--last-name-grey);
  }
</style>
</head>
<body>
<svg class="namecard" viewBox="0 0 828 1200" xmlns="http://www.w3.org/2000/svg" role="img" aria-label="Kiteloft name tag">
  <defs>
    <clipPath id="band-clip">
      <rect x="7" y="75" width="814" height="850"/>
    </clipPath>
  </defs>

  <rect class="namecard__frame" x="3.5" y="3.5" width="821" height="1193"/>

  <text class="namecard__hashtag" x="28" y="57" textLength="410" lengthAdjust="spacingAndGlyphs">#Kiteloft</text>

  <rect class="namecard__band" x="7" y="75" width="814" height="850"/>
  <polygon class="namecard__bubble-tail" points="630,924 622,1033 760,924"/>

  <g clip-path="url(#band-clip)">
    <g class="namecard__first-name">
      <text x="4" y="598" textLength="200" lengthAdjust="spacingAndGlyphs">N</text>
      <text x="202" y="598" textLength="222" lengthAdjust="spacingAndGlyphs">A</text>
      <text x="420" y="598" textLength="250" lengthAdjust="spacingAndGlyphs">M</text>
      <text x="674" y="598" textLength="170" lengthAdjust="spacingAndGlyphs">E</text>
    </g>
    <g class="namecard__last-name">
      <text x="5" y="761" textLength="372" lengthAdjust="spacingAndGlyphs">LAST</text>
      <text x="420" y="761" textLength="440" lengthAdjust="spacingAndGlyphs">NAME</text>
    </g>
  </g>

  <polygon class="namecard__base" points="200,1133 650,1133 685,1193 165,1193"/>
</svg>
</body>
</html>
```